Physiotherapy Referral Pad

-Need a referral pad for physiotherapy to be provided to doctors' offices. I would like it to be simple, not too cluttered and sharp looking so doctors can quickly complete it for clients.

-I have attached my logo which I would like to include. I have also included my business cards to keep the style, font, colors etc consistent.

-I would like to include my slogan
From Our Home To Yours

-I would like it to include services options with tick boxes for Mobile, Clinic, Telehealth, NPKRTW

-I would like for it to say Call to Book or Book Online

-I would like it to include my clinic address:
742 Larkin Crescent
Whitehorse, YT
Y1B2K9

-I would like it to include my contact info:
Gavin Trusk BSc(kin), MPT, CAFCI, IMS
(867)555-0142
physio@trusktherapy.ca

-I would like lines for the following:
Patient Name:
Diagnosis/Recommendations:
(extra lines to fill out patient info)

Physician Signature
Date

Target Market(s)

Physicians to refer clients to physiotherapy

Industry/Entity Type

Physical Therapy

Requirements
Must have
• Clean, concise, easy to look at and find pertinant categories for physicians
Nice to have
• Trusk Therapy color scheme. Please see business cards and website as needed
Should not have
• Not too cluttered or wordy

```html
<!DOCTYPE html>
<html lang="en">
<head>
<meta charset="utf-8">
<title>Trusk Therapy – Referral Pad</title>
<link href="https://fonts.googleapis.com/css2?family=Libre+Baskerville:wght@400;700&family=Roboto:wght@400&display=swap" rel="stylesheet">
<style>
  :root {
    --navy: #243b8a;
    --green: #1a5a36;
    --ink-grey: #555a60;
    --rule: #6b6f75;
    --paper: #fafafa;
    --backdrop: #e2e2e2;
  }
  * { box-sizing: border-box; margin: 0; padding: 0; }
  html, body { width: 1200px; height: 800px; overflow: hidden; }
  body {
    background: var(--backdrop);
    font-family: "Libre Baskerville", Georgia, serif;
    font-weight: 700;
    position: relative;
  }
  .referral-pad {
    position: absolute;
    left: 330px; top: 20px;
    width: 540px; height: 760px;
    background: var(--paper);
    box-shadow: 0 6px 18px rgba(0,0,0,.18);
    overflow: hidden;
  }
  .centered { position: absolute; left: 0; width: 100%; text-align: center; }
  .brand-mark {
    position: absolute; left: 243px; top: 32px;
    width: 54px; height: 54px; border-radius: 50%;
    background: var(--navy);
  }
  .brand-name {
    top: 100px;
    color: var(--green);
    font-size: 26px;
    font-weight: 700;
    letter-spacing: 1px;
    line-height: 1.3;
  }
  .booking-call {
    top: 155px;
    color: var(--navy);
    font-size: 19px;
    font-weight: 700;
    font-variant: small-caps;
    letter-spacing: .3px;
  }
  .contact-line {
    top: 180px;
    font-family: "Roboto", Arial, sans-serif;
    font-weight: 400;
    font-size: 11px;
    color: var(--ink-grey);
    display: flex; justify-content: center; align-items: center; gap: 8px;
  }
  .contact-item { display: inline-flex; align-items: center; gap: 3px; }
  .contact-item svg { width: 11px; height: 11px; }
  .website {
    top: 197px;
    font-family: "Roboto", Arial, sans-serif;
    font-weight: 400;
    font-size: 11px;
    color: var(--ink-grey);
  }
  .website .domain { color: var(--navy); }
  .practitioner-name {
    top: 223px;
    color: var(--green);
    font-size: 25px;
    font-weight: 700;
  }
  .credentials {
    top: 256px;
    color: var(--navy);
    font-size: 11.5px;
    font-weight: 700;
  }
  .credentials .sc { font-variant: small-caps; }
  .service-options {
    top: 285px;
    display: flex; justify-content: center; gap: 7px;
    color: var(--green);
    font-size: 13px;
    font-weight: 700;
  }
  .service-option { display: inline-flex; align-items: center; gap: 5px; }
  .tick-box { width: 12px; height: 12px; border: 1.5px solid var(--green); display: inline-block; }
  .form-field {
    position: absolute; left: 55px; width: 425px;
    display: flex; align-items: flex-end; gap: 8px;
    color: var(--navy);
    font-size: 13px;
    font-weight: 700;
  }
  .form-field .label { white-space: nowrap; line-height: 1; }
  .form-field .label.sc { font-variant: small-caps; font-size: 14px; }
  .form-field .fill-line { flex: 1; border-bottom: 1px solid var(--rule); height: 1px; margin-bottom: -2px; }
  .blank-line {
    position: absolute; left: 55px; width: 425px;
    border-bottom: 1px solid var(--rule);
  }
  .slogan-band {
    position: absolute; left: 0; bottom: 0;
    width: 100%; height: 43px;
    background: var(--navy);
    color: #fff;
    font-size: 19px;
    font-weight: 700;
    letter-spacing: .5px;
    display: flex; align-items: center; justify-content: center;
  }
</style>
</head>
<body>
  <main class="referral-pad">
    <div class="brand-mark"></div>
    <div class="centered brand-name">Trusk Therapy</div>

    <div class="centered booking-call">Call to Book or Book Online</div>

    <div class="centered contact-line">
      <span class="contact-item">
        <svg viewBox="0 0 12 12" aria-hidden="true"><circle cx="6" cy="6" r="6" fill="#243b8a"/><path d="M6 2.5a2.2 2.2 0 0 0-2.2 2.2C3.8 6.4 6 9.3 6 9.3s2.2-2.9 2.2-4.6A2.2 2.2 0 0 0 6 2.5z" fill="#fff"/><circle cx="6" cy="4.7" r=".8" fill="#243b8a"/></svg>
        742 Larkin Crescent Whitehorse, YT Y1B2K9
      </span>
      <span class="contact-item">
        <svg viewBox="0 0 12 12" aria-hidden="true"><circle cx="6" cy="6" r="6" fill="#243b8a"/><path d="M4 3l1.2 1.5-.6.8a4 4 0 0 0 2 2l.8-.6L9 7.9l-.7.9C6 9 3.2 6.1 3.2 3.8z" fill="#fff"/></svg>
        (867)555-0142
      </span>
      <span class="contact-item">
        <svg viewBox="0 0 12 12" aria-hidden="true"><circle cx="6" cy="6" r="6" fill="#243b8a"/><rect x="3" y="4" width="6" height="4.2" rx=".5" fill="#fff"/><path d="M3.2 4.3 6 6.4l2.8-2.1" stroke="#243b8a" stroke-width=".8" fill="none"/></svg>
        physio@trusktherapy.ca
      </span>
    </div>
    <div class="centered website">www.<span class="domain">trusktherapy</span>.ca</div>

    <div class="centered practitioner-name">GAVIN TRUSK</div>
    <div class="centered credentials">BSC<span class="sc">(kin)</span>, MPT, CAFCI, IMS</div>

    <div class="centered service-options">
      <span class="service-option"><span class="tick-box"></span>MOBILE</span>
      <span class="service-option"><span class="tick-box"></span>CLINIC</span>
      <span class="service-option"><span class="tick-box"></span>TELEHEALTH</span>
      <span class="service-option"><span class="tick-box"></span>NPKRTW</span>
    </div>

    <div class="form-field" style="top:356px"><span class="label">PATIENT NAME:</span><span class="fill-line"></span></div>
    <div class="blank-line" style="top:414px"></div>

    <div class="form-field" style="top:445px"><span class="label sc">Diagnosis/Recommendations:</span><span class="fill-line"></span></div>
    <div class="blank-line" style="top:503px"></div>
    <div class="blank-line" style="top:547px;left:58px"></div>

    <div class="form-field" style="top:610px;left:58px"><span class="label sc">Physician Signature</span><span class="fill-line"></span></div>
    <div class="form-field" style="top:655px;left:58px"><span class="label sc">Date</span><span class="fill-line"></span></div>

    <footer class="slogan-band">FROM OUR HOME TO YOURS</footer>
  </main>
</body>
</html>
```